female stress management consultant, doctor, Health & Well-being coach needs a wordpress theme

I am a Stress management consultant, General Practitioner and Health and Well-Being coach who is targeting mainly surgeries/hospitals and corporate business.
I have my own URL drhalvoreskby.com and the hosting.
I need a WordPress Website that is easy to maintain and edit to regularly change the content (copy/pictures/action buttons/banners).
I want my website to look professional and elegant for corporate businesses and managers to feel they can trust me and my expertise. At the same time, the website should have a warm and welcoming feel to it. It should feel uplifting and very positive.
I am open to colour suggestions, but please incorporate the following two colours: #F18877 and #D2BB7A. For fonts I prefer grey over black (like #777777).
The website needs to create an impression of "know like and trust".
The website should have a sign-up button for a newsletter, multiple contact buttons over the home page - to write an email to me, contact details top and bottom and the possibility to have a video on the home page top instead of a picture (Best would be that I can change from picture to video to picture in the future without needing a designer). A video that can run in the background with text laid over. A bit like on this website from Tessa Grublin: https://www.tessagrublin.com.
I need 5 pages: Home, About, Services, Contact, free resources. I do NOT need an e-commerce or booking facility as I will neither sell nor let people book through my website. I don't need a blog either.
All the pages need to have a link to my other website (brightpathdaily.co.uk) and it needs to state that the linked website (brightpathdaily) is my website with a blog and for private customers.
Please use the photos I attached if possible. Me with the dogs for the "about" section.

Websites I like: https://www.orlaqvx.com, tessagrublin.com, https://pennyrastrick.com (this site is too dark for my liking, but the layout has a simple navigation layout, the important buttons are right up at the side (LinkedIn/social media/CTA), is minimalistic - hence easy to find the important bits).

surgeries/doctor offices, hospitals, corporate business

Health and well-being

• see project description
• see project description

```html
<!DOCTYPE html>
<html lang="en">
<head>
<meta charset="utf-8">
<title>Halvoreskby – Create a life you love living</title>
<link rel="stylesheet" href="https://fonts.googleapis.com/css2?family=Crimson+Pro:ital,wght@0,500;0,700;1,400;1,500&family=Libre+Baskerville:wght@700&family=Roboto:ital,wght@0,400;0,500;0,700;1,400&display=swap">
<style>
:root{
  --coral:#F18877;
  --coral-dark:#e9735f;
  --gold:#D2BB7A;
  --grey:#777777;
  --ink:#2b2b2b;
  --blush:#f3c4bb;
  --paper:#f5f5f5;
  --footer:#333333;
  --footer-deep:#222222;
  --white:#ffffff;
}
*{box-sizing:border-box;margin:0;padding:0}
html,body{width:1200px;height:3289px;overflow:hidden}
body{position:relative;font-family:"Roboto",Arial,sans-serif;color:var(--grey);background:var(--white)}
.serif{font-family:"Crimson Pro",Georgia,serif}
section,header,footer{position:absolute;left:0;width:1200px}
.abs{position:absolute}
.btn{position:absolute;display:flex;align-items:center;justify-content:center;font-weight:700;font-size:11px;text-transform:uppercase;letter-spacing:.3px;text-decoration:none}
.btn-coral{background:var(--coral);color:var(--white)}
.btn-outline{border:1.5px solid var(--coral);color:var(--ink);background:var(--white);text-transform:none;font-size:12px;font-weight:500}
.eyebrow{font-size:9px;font-weight:700;letter-spacing:1px;color:var(--ink);text-transform:uppercase}
.placeholder{position:absolute}

/* header + hero */
.hero{top:0;height:486px;background:radial-gradient(circle at 70% 45%,#a6e84e 0,#7fd21e 45%,#6cc018 70%,#4e9a10 100%)}
.hero-shade{position:absolute;left:0;top:0;width:1200px;height:90px;background:linear-gradient(#000a 0,#0000 100%)}
.hero-photo{left:690px;top:77px;width:345px;height:409px;background:linear-gradient(160deg,#e9c49b,#c98c63 60%,#55607e);border-radius:160px 160px 0 0}
.logo{position:absolute;display:flex;align-items:center;gap:8px}
.logo-dot{width:30px;height:30px;border-radius:50%;background:var(--coral)}
.logo-name{font-family:"Crimson Pro",Georgia,serif;font-style:italic;font-size:27px;color:var(--white);line-height:1}
.logo-tag{font-family:"Crimson Pro",Georgia,serif;font-style:italic;font-size:11px;color:var(--white);margin-top:1px}
.nav{position:absolute;left:449px;top:31px;display:flex;gap:28px}
.nav a{color:var(--white);font-size:11px;font-weight:700;text-decoration:none;letter-spacing:.4px}
.hero h1{position:absolute;left:214px;top:140px;font-family:"Libre Baskerville",Georgia,serif;font-size:39px;line-height:50px;color:#111}
.hero p{position:absolute;left:216px;top:304px;width:405px;font-size:14px;line-height:23px;color:#222}

/* newsletter band */
.newsletter{top:486px;height:108px;background:var(--blush)}
.newsletter h2{position:absolute;left:258px;top:20px;font-size:26px;font-style:italic;font-weight:400;color:var(--ink)}
.newsletter p{position:absolute;left:258px;top:56px;width:300px;font-size:10px;line-height:14px;color:#8a6c66}
.field{position:absolute;background:var(--white);border:1px solid #e5b2aa;font-size:11px;font-style:italic;color:var(--grey);display:flex;align-items:center;padding-left:12px}

/* about */
.about{top:594px;height:430px}
.about-photo{left:0;top:0;width:605px;height:430px;background:linear-gradient(135deg,#6f8a3a,#b9c77a 45%,#c59a6c 75%,#5a6574)}
.about h2{position:absolute;left:659px;top:84px;font-size:38px;line-height:42px;font-style:italic;font-weight:500;color:var(--ink)}
.about h2 span{color:var(--coral)}
.about p{position:absolute;left:659px;top:186px;width:326px;font-size:13px;line-height:20px}

/* roles */
.roles{top:1024px;height:267px;background:var(--paper)}
.role{position:absolute;top:0;height:267px;width:262px;text-align:center}
.role+.role{border-left:1px solid #e2e2e2}
.role-icon{width:48px;height:48px;border-radius:50%;background:var(--white);margin:36px auto 0;display:flex;align-items:center;justify-content:center;box-shadow:0 1px 3px #0002}
.role h3{font-size:22px;font-style:italic;font-weight:500;color:var(--coral);margin-top:8px}
.role p{font-size:11px;line-height:16.3px;margin:6px auto 0;width:228px}
.role .more{color:var(--coral)}

/* sunset banner */
.banner{top:1291px;height:195px;background:linear-gradient(#8c7f86 0,#d7a77f 40%,#c98653 62%,#7a5a48 100%)}
.banner .eyebrow{position:absolute;left:0;width:1200px;text-align:center;top:33px;color:var(--white)}
.banner blockquote{position:absolute;left:0;width:1200px;top:53px;text-align:center;font-size:23px;line-height:28px;font-style:italic;color:var(--white)}

/* shape the life */
.shape{top:1486px;height:431px}
.shape h2{position:absolute;left:212px;top:88px;font-size:40px;line-height:41px;font-style:italic;font-weight:500;color:var(--ink);letter-spacing:.5px}
.shape h2 span{color:var(--coral)}
.shape p{position:absolute;left:212px;top:240px;width:322px;font-size:13px;line-height:20px}

/* resources */
.resources{top:1917px;height:532px;background:var(--blush)}
.resources h2{position:absolute;left:0;width:1200px;top:66px;text-align:center;font-size:38px;font-style:italic;font-weight:400;color:var(--ink)}
.card{position:absolute;top:135px;width:250px;height:347px;background:var(--white)}
.card-img{width:250px;height:153px}
.card h3{margin:16px 0 0 19px;font-size:18px;font-style:italic;font-weight:500;color:var(--ink)}
.card p{margin:4px 19px 0;font-size:9.7px;line-height:16px}

/* testimonials */
.testimonials{top:2449px;height:393px;text-align:center}
.testimonials h2{position:absolute;left:0;width:1200px;top:44px;font-size:42px;font-style:italic;font-weight:400;color:var(--ink);letter-spacing:1px}
.testimonials h3{position:absolute;left:0;width:1200px;top:114px;font-size:19px;font-style:italic;font-weight:500;color:var(--ink)}
.testimonials blockquote{position:absolute;left:278px;width:644px;top:150px;font-size:13px;line-height:20px;font-style:italic;color:#8a8a8a}
.dot{position:absolute;top:2788px;width:9px;height:9px;background:#999}

/* call to action */
.cta{top:2842px;height:226px;background:var(--coral)}
.cta h2{position:absolute;left:0;width:1200px;top:40px;text-align:center;font-size:34px;line-height:38px;font-style:italic;font-weight:400;color:var(--white);letter-spacing:.5px}

/* footer */
.footer{top:3068px;height:221px;background:var(--footer)}
.footer .about-line{position:absolute;left:214px;top:90px;width:212px;font-style:italic;font-size:12px;line-height:17px;color:#ccc}
.links{position:absolute;top:38px;list-style:none}
.links li{font-size:10px;color:#bbb;height:22.3px}
.footer h2{position:absolute;left:740px;top:34px;font-size:20px;line-height:22px;font-style:italic;font-weight:400;color:#ddd}
.social{position:absolute;top:3217px;width:22px;height:22px;border-radius:50%;border:1.5px solid #ccc}
.copyright{position:absolute;left:0;top:208px;width:1200px;height:13px;background:var(--footer-deep);text-align:center;font-size:7px;line-height:13px;color:#999}
</style>
</head>
<body>

<header class="hero">
  <div class="placeholder hero-photo" role="img" aria-label="Portrait photo of the smiling doctor in a striped top"></div>
  <div class="hero-shade"></div>
  <div class="logo" style="left:214px;top:20px">
    <div class="logo-dot"></div>
    <div><div class="logo-name">Halvoreskby</div><div class="logo-tag">Create a life you love living</div></div>
  </div>
  <nav class="nav">
    <a href="#">HOME</a><a href="#">ABOUT</a><a href="#">SERVICES</a><a href="#">FREE RESOURCES</a><a href="#">CONTACT</a>
  </nav>
  <a class="btn btn-coral" style="left:844px;top:22px;width:143px;height:30px;font-size:9.5px">Get a free consultant</a>
  <h1>Live a Healthy<br>&amp; Best Life With<br>Full of Joy!</h1>
  <p>I am a Stress management consultant, General Practitioner and Health and Well-Being coach who is targeting mainly surgeries/hospitals and corporate business.</p>
  <a class="btn btn-coral" style="left:216px;top:392px;width:145px;height:28px;font-size:9.5px">Get a free consultant</a>
</header>

<section class="newsletter">
  <h2 class="serif">Subscribe to Our Newsletter</h2>
  <p>Get regular inspiration for the Health and Well-Being, and keep up with the healthcare stories that matter.</p>
  <div class="field" style="left:632px;top:35px;width:238px;height:37px">Your Email Address</div>
  <a class="btn btn-coral" style="left:870px;top:35px;width:79px;height:37px;font-size:10px">Subscribe</a>
</section>

<section class="about">
  <div class="placeholder about-photo" role="img" aria-label="Photo of the doctor outdoors kneeling with her two dogs"></div>
  <div class="eyebrow abs" style="left:659px;top:64px">Hello !</div>
  <h2 class="serif">I’m <span>Doctor<br>Halvoreskby.</span></h2>
  <p>With over 30 years of being a doctor, I’ve met countless people facing ongoing health issues and struggles that couldn’t be solved solely through conventional medicine. That’s why it’s so important to embrace a holistic approach in our quest for balance, shifting from discomfort to vitality and contentment.</p>
  <a class="btn btn-outline" style="left:659px;top:332px;width:114px;height:32px">Read More</a>
</section>

<section class="roles">
  <div class="role" style="left:206px">
    <div class="role-icon"><svg width="26" height="26" viewBox="0 0 26 26" fill="none" stroke="#333" stroke-width="2.2" stroke-linecap="round"><path d="M6 3v7a5 5 0 0 0 10 0V3"/><path d="M11 15v3a4 4 0 0 0 8 0v-3"/><circle cx="19" cy="12" r="2.5"/></svg></div>
    <h3 class="serif">Consultant</h3>
    <p>If you’re feeling stuck, uncertain, or struggling with your health or well-being, one-on-one coaching can provide the guidance and support you need. Through working together to explore, we can identify solutions and help you unlock your full potential, empowering...<br><span class="more">[ Read more... ]</span></p>
  </div>
  <div class="role" style="left:469px">
    <div class="role-icon"><svg width="26" height="26" viewBox="0 0 26 26" fill="none" stroke="#333" stroke-width="2.2" stroke-linejoin="round"><rect x="3" y="7" width="20" height="15" rx="2"/><path d="M9 7V4h8v3"/><path d="M13 11v7M9.5 14.5h7"/></svg></div>
    <h3 class="serif">Practitioner</h3>
    <p>Medical doctor and General Practitioner, certified Health and Well-being Coach hold a doctorate degree in virology (PhD); I’m a Meditation teacher, Creative Wellness Coach and Teacher, artist, friend, mum, and a humble human being who has a wealth...<br><span class="more">[ Read more... ]</span></p>
  </div>
  <div class="role" style="left:730px">
    <div class="role-icon"><svg width="28" height="28" viewBox="0 0 28 28" fill="#333"><circle cx="7" cy="7" r="3"/><path d="M3 12h8l3 4-2 1-2-2v10H5v-8H3z"/><rect x="12" y="3" width="13" height="10" fill="none" stroke="#333" stroke-width="1.8"/><circle cx="16" cy="19" r="2"/><circle cx="22" cy="19" r="2"/><path d="M13 25a3 3 0 0 1 6 0zM19 25a3 3 0 0 1 6 0z"/></svg></div>
    <h3 class="serif">Coach</h3>
    <p>I’m a Meditation teacher, Creative Wellness Coach and Teacher, artist, friend, mum, and a humble human being who has a wealth of knowledge on how to lead a happy and healthy life. I offer a variety of engaging and informative workshops and online courses...<br><span class="more">[ Read more... ]</span></p>
  </div>
</section>

<section class="banner" role="img" aria-label="Sunset over the sea with palm trees on a sandy beach">
  <div class="eyebrow">I help you find answers</div>
  <blockquote class="serif">The secret to living a joyful, vibrant life lies in nurturing<br>every aspect of yourself, not just your physical body.</blockquote>
  <a class="btn btn-coral" style="left:531px;top:134px;width:143px;height:26px;font-size:9.5px">Get a free consultant</a>
</section>

<section class="shape">
  <div class="eyebrow abs" style="left:212px;top:60px">You have the power to</div>
  <h2 class="serif"><span>Shape the life</span><br>you truly love !<br>Every single day!</h2>
  <p>Believe it or not, your influence over your health and well-being is even greater than you realise. It’s easier than you think! Let’s create a life that brings you joy. I’m here for you!</p>
  <a class="btn btn-outline" style="left:212px;top:340px;width:114px;height:32px">Read More</a>
  <svg class="abs" style="left:672px;top:40px" width="350" height="350" viewBox="0 0 350 350" role="img" aria-label="Video thumbnail: open hands releasing butterflies into a warm sunset">
    <defs>
      <linearGradient id="glow" x1="0" y1="0" x2="0" y2="1">
        <stop offset="0" stop-color="#f7d9a6"/><stop offset=".5" stop-color="#f0a752"/><stop offset="1" stop-color="#a2542a"/>
      </linearGradient>
    </defs>
    <path d="M40 95C70 40 170 5 265 18c60 8 80 55 70 130-8 70-40 155-130 180C120 352 40 320 18 235 4 180 15 135 40 95z" fill="none" stroke="var(--coral-dark)" stroke-width="5"/>
    <path d="M46 102C76 52 170 20 258 30c52 7 70 50 62 118-8 66-38 146-118 168C126 336 52 306 32 230 20 180 26 138 46 102z" fill="url(#glow)"/>
    <circle cx="175" cy="150" r="28" fill="#fff"/>
    <path d="M166 136l22 14-22 14z" fill="var(--coral)"/>
    <text x="178" y="228" text-anchor="middle" font-family="Crimson Pro,Georgia,serif" font-style="italic" font-size="27" fill="#fff">Begin again today</text>
    <text x="178" y="258" text-anchor="middle" font-family="Crimson Pro,Georgia,serif" font-style="italic" font-size="27" fill="#fff">online gathering</text>
  </svg>
</section>

<section class="resources">
  <div class="eyebrow abs" style="left:0;width:1200px;text-align:center;top:50px">Our free resources</div>
  <h2 class="serif">that help you live your best life</h2>
  <article class="card" style="left:212px">
    <div class="card-img" role="img" aria-label="Plate of fresh salad beside a glass of white wine" style="background:linear-gradient(135deg,#8da0d8,#eef0f5 55%,#c9d0e0)"></div>
    <h3 class="serif">Eat Well</h3>
    <p>I’ve met countless people facing ongoing health issues and struggles that couldn’t be solved solely through conventional medicine. That’s why it’s so important to embrace a holistic approach in our quest for balance..</p>
    <a class="btn btn-outline" style="left:19px;top:290px;width:114px;height:32px">Get Inspired</a>
  </article>
  <article class="card" style="left:475px">
    <div class="card-img" role="img" aria-label="Joyful woman with arms raised among green trees" style="background:linear-gradient(135deg,#4f8b34,#9cc870 50%,#7d8fc4)"></div>
    <h3 class="serif">Live Healthy</h3>
    <p>The secret to living a joyful, vibrant life lies in nurturing every aspect of yourself, not just your physical body. Surprisingly, it’s easier as you might think to harmonize your body, mind, and spirit and experience optimal well-being...</p>
    <a class="btn btn-outline" style="left:19px;top:290px;width:114px;height:32px">Get Inspired</a>
  </article>
  <article class="card" style="left:738px">
    <div class="card-img" role="img" aria-label="Close portrait of the smiling doctor" style="background:linear-gradient(135deg,#5f6d3c,#d8b08c 55%,#a47a5c)"></div>
    <h3 class="serif">It’s Been So Easy</h3>
    <p>They provide knowledge, support, and motivation for positive change. Engaging in these discussions connects you to a community, empowers you with insights, and promotes self-awareness. Get ready for</p>
    <a class="btn btn-outline" style="left:19px;top:290px;width:114px;height:32px">Get Inspired</a>
  </article>
</section>

<section class="testimonials">
  <h2 class="serif">Testimonials</h2>
  <h3 class="serif">Working with Dr Halvoreskby helped me to appreciate myself more.</h3>
  <blockquote>The workshop has allowed me to appreciate myself more. For what I am. The quality of delivery is what made the experience. Dr Halvoreskby’s understanding of the guided meditations helped enormously. Being in an exclusive, supportive and safe environment allowed me to get in touch with elements of myself that I was shy of. I’d love more people to be able to access this and to experience this quality of experience.</blockquote>
  <div class="placeholder" role="img" aria-label="Client portrait" style="left:534px;top:249px;width:54px;height:54px;background:linear-gradient(#d9d4cc,#b7a18a)"></div>
  <div class="abs" style="left:600px;top:258px;text-align:left">
    <div style="color:var(--coral);font-size:15px">Mirel T.</div>
    <div style="font-size:11px;margin-top:2px">Private Client</div>
  </div>
</section>
<div class="dot" style="left:572px;background:var(--coral)"></div>
<div class="dot" style="left:588px"></div>
<div class="dot" style="left:604px"></div>
<div class="dot" style="left:620px"></div>

<section class="cta">
  <h2 class="serif">Discover Simple Steps to Restore Your<br>Happiness and Health Today!</h2>
  <a class="btn" style="left:494px;top:146px;width:212px;height:31px;background:var(--white);color:var(--ink);font-size:10.5px">Get a free consultant today!</a>
</section>

<footer class="footer">
  <div class="logo" style="left:214px;top:34px">
    <div class="logo-dot"></div>
    <div><div class="logo-name" style="color:#e6e6e6">Halvoreskby</div><div class="logo-tag" style="color:#bbb">Create a life you love living</div></div>
  </div>
  <p class="about-line">The time that you invest in yourself, your health and your happiness will be the best investment you can make. You can’t buy happiness, but you can create it.</p>
  <ul class="links" style="left:469px"><li>Home</li><li>About</li><li>Services</li><li>Coaching</li><li>Free Resources</li><li>Free Talk Health</li></ul>
  <ul class="links" style="left:599px"><li>Privacy Policy</li><li>Disclaimer</li><li>Health Advice</li><li>Virtual Summit</li><li>News &amp; Blog</li><li>Contact</li></ul>
  <h2 class="serif">Join our newsletter to get<br>the latest news and tips.</h2>
  <div class="field" style="left:738px;top:93px;width:167px;height:31px;background:#6a6a6a;border:none;color:#ddd;font-style:normal;font-size:10px">Your Email Address</div>
  <a class="btn btn-coral" style="left:905px;top:93px;width:82px;height:31px;text-transform:none;font-size:11px">Join Now</a>
  <div class="copyright">© 2020 Dr Halvoreskby. All rights reserved. Privacy and Cookies</div>
</footer>
<div class="social" style="left:740px"></div>
<div class="social" style="left:778px"></div>
<div class="social" style="left:813px"></div>
<div class="social" style="left:851px"></div>
<div class="social" style="left:889px"></div>

</body>
</html>
```